Geschäftspapiere für Vermittlung von Baudienstleistungen
Zielgruppe
Vermittlung von Baudienstleistungen und digitalen Produkten in diesem Zusammenhang über eine künftige
Webseite und social Media. Das Unternehmen: LOMIRA Werk GmbH, Holunderpfad 12, 51588 Tannfeld.
Öffentlicher Auftritt: www.boden-heldo.de mit dem Logo: Boden Heldo.
Als Vorlage haben wir bereits ein Logo Design und Visitenkarten erstellt und möchten dazu passend das Briefpapier entworfen haben. Unsere Kunden sind Privatpersonen 40+, Privathaushalte,
Aufgabenstellung
Logo Design und Visitenkarte als Vorlage für Designrichtung.
Vorderseite elegant, Stilsicher aber nicht überfüllt. Hingucker!
Farben sind Moosgrün und grau. Farbwerte können aus der Vorlage extrahiert werden.
Stil 'Halfton' soll beim Design eingearbeitet werden. Vor allem im unteren Bereich wo wir die
Firemenangaben haben möchten. Adresse | Rechtliches | Bankverbindung | Tel/Fax/Mobil | Kontakt

```html
<!DOCTYPE html>
<html lang="de">
<head>
<meta charset="utf-8">
<title>Briefbogen Boden Heldo</title>
<link href="https://fonts.googleapis.com/css2?family=Arimo:wght@400;700&family=Open+Sans:wght@300&display=swap" rel="stylesheet">
<style>
  :root {
    --moss: #7fa832;
    --moss-tint: #eef3df;
    --grey: #5f6062;
    --grey-dark: #3a3a3c;
    --grey-light: #c9c9c9;
    --backdrop: #e6e6e6;
    --paper: #ffffff;
  }
  * { margin: 0; padding: 0; box-sizing: border-box; }
  html, body { width: 1200px; height: 1105px; overflow: hidden; }
  body {
    background: var(--backdrop);
    font-family: "Arimo", Arial, sans-serif;
    color: var(--grey);
    position: relative;
  }
  .letterhead {
    position: absolute;
    left: 246px; top: 52px;
    width: 707px; height: 1000px;
    background: var(--paper);
    box-shadow: 0 6px 20px rgba(0,0,0,0.18);
    overflow: hidden;
  }
  .header-halftone {
    position: absolute; right: 0; top: 0;
    width: 360px; height: 230px;
    background: radial-gradient(ellipse at 85% 35%, var(--moss-tint) 0%, rgba(238,243,223,0.6) 45%, rgba(255,255,255,0) 75%);
  }
  .footer-halftone {
    position: absolute; left: 0; bottom: 0;
    width: 360px; height: 150px;
    background: radial-gradient(ellipse at 15% 80%, #ececec 0%, rgba(236,236,236,0.5) 45%, rgba(255,255,255,0) 75%);
  }
  .rule { position: absolute; height: 1.5px; background: var(--moss); }
  .rule-top { left: 20px; top: 36px; width: 420px; }
  .rule-brand { left: 430px; top: 214px; width: 277px; }
  .rule-footer { left: 70px; top: 862px; width: 637px; }
  .brand {
    position: absolute; right: 44px; top: 112px;
    text-align: right;
  }
  .brand-name {
    display: flex; align-items: center; justify-content: flex-end; gap: 10px;
    font-weight: 700; font-size: 38px; color: var(--moss);
    letter-spacing: 0.5px; line-height: 1; white-space: nowrap;
  }
  .brand-mark { width: 18px; height: 18px; background: var(--moss); }
  .brand-tagline {
    margin-top: 12px;
    font-size: 14.5px; color: var(--grey-dark); letter-spacing: 0.3px; white-space: nowrap;
  }
  .sender-line {
    position: absolute; left: 80px; top: 150px;
    font-size: 7.5px; color: var(--grey); white-space: nowrap;
    padding-bottom: 3px; border-bottom: 0.8px solid var(--grey-light);
  }
  .sender-line .company { color: var(--moss); }
  .sender-line .sep { color: var(--moss); margin: 0 3px; }
  .fold-mark { position: absolute; left: 0; width: 22px; height: 0.8px; background: var(--grey-light); }
  .fold-upper { top: 354px; }
  .fold-lower { top: 707px; }
  .side-company {
    position: absolute; left: 50px; top: 840px;
    transform: rotate(-90deg); transform-origin: left top;
    font-family: "Open Sans", Arial, sans-serif; font-weight: 300;
    font-size: 24px; color: var(--grey-dark); white-space: nowrap;
  }
  .side-mark {
    position: absolute; left: 30px; top: 850px;
    width: 40px; height: 40px; border-radius: 50%; background: var(--moss);
  }
  .footer {
    position: absolute; left: 232px; top: 884px;
    display: flex;
    font-size: 8.5px; line-height: 1.5; color: var(--grey-dark);
    white-space: nowrap;
  }
  .footer-col { padding: 0 14px; }
  .footer-col + .footer-col { border-left: 0.8px solid var(--grey-light); }
  .footer-col:first-child { padding-left: 0; }
  .footer-brand { font-weight: 700; font-size: 10.5px; color: var(--moss); }
  .accent { color: var(--moss); }
  .contact-row { display: flex; align-items: center; gap: 6px; }
  .contact-row svg { width: 9px; height: 9px; fill: var(--moss); flex: none; }
</style>
</head>
<body>
  <main class="letterhead">
    <div class="header-halftone" role="img" aria-label="Halbton-Punktraster in zartem Moosgrün"></div>
    <div class="footer-halftone" role="img" aria-label="Halbton-Punktraster in hellem Grau"></div>

    <div class="rule rule-top"></div>
    <div class="rule rule-brand"></div>
    <div class="rule rule-footer"></div>

    <div class="brand">
      <div class="brand-name"><span class="brand-mark"></span>Boden Heldo</div>
      <div class="brand-tagline">Bewahren | Sichern | Erneuern</div>
    </div>

    <p class="sender-line"><span class="company">LOMIRA Werk GmbH</span><span class="sep">|</span>Holunderpfad 12<span class="sep">|</span>51588 Tannfeld</p>

    <div class="fold-mark fold-upper"></div>
    <div class="fold-mark fold-lower"></div>

    <p class="side-company">LOMIRA Werk GmbH</p>
    <div class="side-mark"></div>

    <footer class="footer">
      <div class="footer-col">
        <div class="footer-brand">Boden Heldo</div>
        <div class="accent">LOMIRA Werk GmbH</div>
        <div>Holunderpfad 12</div>
        <div>51588 Tannfeld</div>
      </div>
      <div class="footer-col">
        <div class="contact-row"><svg viewBox="0 0 10 10"><path d="M2 0.5 L3.6 0.5 L4.2 2.8 L3 3.6 Q4 5.8 6.4 7 L7.2 5.8 L9.5 6.4 L9.5 8 Q9.5 9.5 8 9.5 Q0.5 9 0.5 2 Q0.5 0.5 2 0.5Z"/></svg>02261 - 4 38 21 90</div>
        <div class="contact-row"><svg viewBox="0 0 10 10"><path d="M2.5 0 H7.5 V10 H2.5Z M3.3 1 V8 H6.7 V1Z" fill-rule="evenodd"/></svg>0171 - 482 93 16</div>
        <div class="contact-row"><svg viewBox="0 0 10 10"><path d="M0 2 H10 V8 H0Z M1 2.8 L5 5.6 L9 2.8 V3.8 L5 6.6 L1 3.8Z" fill-rule="evenodd"/></svg>brettmer@boden-heldo.de</div>
        <div class="contact-row"><svg viewBox="0 0 10 10"><circle cx="5" cy="5" r="4.5" fill="none" stroke="#7fa832" stroke-width="1"/><path d="M0.5 5 H9.5 M5 0.5 Q2 5 5 9.5 Q8 5 5 0.5" fill="none" stroke="#7fa832" stroke-width="0.8"/></svg>www.boden-heldo.de</div>
      </div>
      <div class="footer-col">
        <div class="accent">Bankverbindung:</div>
        <div>Weserländische Bürgerbank</div>
        <div>IBAN: DE41 XXXX 0007 XXXX 3816 02</div>
        <div>BIC: &nbsp;&nbsp;XXXXW7BXXX</div>
        <div>Steuer-Nr. 31/XXX/07XXX</div>
      </div>
    </footer>
  </main>
</body>
</html>
```